Flyer design for webdesign company

create a flyer that can be printed or sent as an email. The flyer needs to be professional, modern and engaging.

Reason: opportunity for all designers to get their designs in.

Target Market(s)

business owners that do not have a website

Industry/Entity Type

It Company

Font styles to use
Sans Serif

```html
<!DOCTYPE html>
<html lang="en">
<head>
<meta charset="utf-8">
<title>novasites – Website Flyer</title>
<link rel="stylesheet" href="https://fonts.googleapis.com/css2?family=Arimo:wght@400;700&family=Roboto+Condensed:wght@400&display=swap">
<style>
  :root {
    --sun: #f0b91e;
    --orange: #ee6a24;
    --brand-orange: #ef8b2c;
    --lime: #8dc63f;
    --sea: #4a9c9b;
    --aqua: #1aaeae;
    --crimson: #b52a4a;
    --pink: #e63e8e;
    --slate: #616161;
    --ink: #555555;
    --night: #363c44;
    --line: #9a9a9a;
    --white: #ffffff;
  }
  * { margin: 0; padding: 0; box-sizing: border-box; }
  html, body { width: 857px; height: 1200px; overflow: hidden; background: var(--white); }
  body { font-family: "Arimo", Arial, sans-serif; }
  .flyer { position: relative; width: 857px; height: 1200px; overflow: hidden; background: var(--white); }

  .url-band {
    position: absolute; left: 0; top: 0; width: 100%; height: 124px;
    background: var(--sun); color: var(--white);
    text-align: center; padding-top: 58px;
    font-size: 31px; line-height: 36px; font-weight: 700; letter-spacing: 0.3px;
  }

  .brand { position: absolute; left: 68px; top: 150px; width: 280px; }
  .brand-dot {
    display: block; width: 140px; height: 140px; border-radius: 50%;
    background: var(--brand-orange); margin: 10px 0 0 62px;
  }
  .brand-name {
    display: block; margin-top: 38px; font-size: 42px; color: var(--brand-orange);
    font-weight: 400; letter-spacing: 0.5px;
  }

  .headline {
    position: absolute; left: 400px; top: 186px; width: 394px; text-align: center;
    font-weight: 700; color: var(--ink); font-size: 34px; line-height: 39px;
  }
  .headline .money { display: block; margin-top: 14px; color: var(--brand-orange); }

  .connectors { position: absolute; left: 0; top: 0; }

  .bubble {
    position: absolute; border-radius: 50%;
    display: flex; align-items: center; justify-content: center;
    text-align: center; color: var(--white); font-size: 21px; line-height: 27px;
  }
  .bubble.available { left: 392px; top: 408px; width: 156px; height: 156px; background: var(--orange);
    font-family: "Roboto Condensed", "Arial Narrow", sans-serif; font-size: 19px; line-height: 27px; }
  .bubble.social { left: 580px; top: 369px; width: 168px; height: 168px; background: var(--lime); }
  .bubble.limited { left: 137px; top: 473px; width: 186px; height: 186px; background: var(--sea);
    font-size: 20px; }
  .bubble.designs { left: 624px; top: 547px; width: 186px; height: 186px; background: var(--crimson); }
  .bubble.pricing { left: 368px; top: 570px; width: 214px; height: 214px; background: var(--sun);
    font-size: 32px; line-height: 36px; font-weight: 700; }
  .bubble.pricing .label { color: var(--ink); }
  .bubble.stat { left: 110px; top: 686px; width: 192px; height: 192px; background: var(--pink);
    font-size: 20px; line-height: 24px; }
  .bubble.compete { left: 334px; top: 796px; width: 180px; height: 180px; background: var(--aqua); }
  .bubble.losing { left: 637px; top: 762px; width: 182px; height: 182px; background: var(--slate); }

  .call-band {
    position: absolute; left: 0; top: 1000px; width: 100%; height: 122px; background: var(--lime);
  }
  .call-band .call {
    position: absolute; left: 58px; top: 36px; color: var(--white); font-size: 33px;
  }
  .bubble.daily { left: 485px; top: 922px; width: 214px; height: 214px; background: var(--sun);
    font-size: 36px; line-height: 42px; font-weight: 700; z-index: 2; }

  .footer-band {
    position: absolute; left: 0; top: 1122px; width: 100%; height: 78px; background: var(--night);
    color: var(--white); font-size: 27px; padding: 10px 0 0 56px;
  }
</style>
</head>
<body>
<main class="flyer">
  <header class="url-band">WWW.NOVASITES-WEB.COM</header>

  <div class="brand">
    <span class="brand-dot"></span>
    <span class="brand-name">novasites</span>
  </div>

  <h1 class="headline">ATTRACT MORE<br>CUSTOMERS<span class="money">MAKE MORE MONEY</span></h1>

  <svg class="connectors" width="857" height="1200" viewBox="0 0 857 1200" aria-hidden="true">
    <g stroke="var(--line)" stroke-width="1">
      <line x1="326" y1="534" x2="386" y2="510"/>
      <line x1="552" y1="530" x2="622" y2="602"/>
      <line x1="314" y1="620" x2="374" y2="646"/>
      <line x1="580" y1="658" x2="610" y2="660"/>
      <line x1="309" y1="742" x2="382" y2="726"/>
      <line x1="483" y1="779" x2="482" y2="811"/>
      <line x1="562" y1="738" x2="642" y2="781"/>
    </g>
  </svg>

  <div class="bubble available">Beautiful Website<br>Available Now</div>
  <div class="bubble social">Social Media<br>setup options<br>(Searchly &amp;<br>Friendbook)</div>
  <div class="bubble limited">Limited to<br>ONLY 4 WEBSITES<br>per area.<br>Don’t miss out!</div>
  <div class="bubble designs">Smart, clean<br>website designs<br>($3000 Value.<br>No extra charge)</div>
  <div class="bubble pricing"><div><span class="label">PRICING:</span><br>ONLY<br>$99/MONTH</div></div>
  <div class="bubble stat">97%<br>of people<br>look online for<br>businesses.<br>You need a<br>website</div>
  <div class="bubble compete">Beat your<br>competition with<br>better visibility<br>and credibility</div>
  <div class="bubble losing">You’re losing<br>many customers<br>by not having a<br>website</div>

  <section class="call-band">
    <p class="call">Call Today1-800-555-0142</p>
  </section>
  <div class="bubble daily">ONLY<br>$3<br>A DAY</div>

  <footer class="footer-band">Stop wasting money on mailers and print advertising</footer>
</main>
</body>
</html>
```